Create a pouch design for a new sports supplement product

Dimensions are 235mm (width) x 335mm (length) x 110mm (gusset)
File 1 - Extension of design brief please read both briefs
File 2 - Is 2 potential pouches this is just to give you a better example of size the dimensions are for the pouch on the right. This picture is not to give you design ideas as I am not very keen on either of these designs.
We need a design to be printed onto the pouches of our whey protein product. The brand name is 'Stellar Fuelworks' and needs to be displayed on the packaging either just writing or a simple logo design. I am not the most creative person in the world but have put together a more detailed brief listing some of the key information that needs to be included on the pouch (See attachment) Please feel free if you have experience of this the sports supplement market or have different ideas then please feel free to explore them.
The pouch would either be printed straight onto the pouch, or possibly just a printed label (front & back) to be stuck onto the pouch. Please design either or both.
Open to different colour schemes. Design has to be modern looking and eye-catching.
Some key points;
High quality whey protein concentrate
All Natural
Soy free
Great tasting
Please google image search 'protein pouches' to see other designs if your not familiar with the sports supplement market.
Any questions feel free to ask.
Updates
Hi, Thanks for all your design! I am really busy at the moment so haven't had chance to give feedback and have a proper look through all the designs. I have extended the time frame to give myself chance to give proper feedback and see any changes needed. Expect feedback sunday at the latest, and I will be pick a design early next week.
Target Market(s)
Sports supplement market. Product is a whey protein shake
Industry/Entity Type
Nutrition
Look and feel
Each slider illustrates characteristics of the customer's brand and the style your logo design should communicate.

```html
<!DOCTYPE html>
<html lang="en">
<head>
<meta charset="utf-8">
<title>Stellar Fuelworks – Natural Whey Protein Pouch</title>
<link href="https://fonts.googleapis.com/css2?family=Play:wght@400;700&display=swap" rel="stylesheet">
<style>
  :root {
    --stage: #d4d4d4;
    --pouch-light: #f7f7f7;
    --pouch-mid: #e6e6e6;
    --brand-red: #e3171b;
    --ink: #161616;
    --white: #ffffff;
  }
  * { margin: 0; padding: 0; box-sizing: border-box; }
  html, body { width: 1200px; height: 900px; overflow: hidden; }
  body { background: var(--stage); font-family: "Play", sans-serif; color: var(--ink); }

  .pouch {
    position: absolute; left: 410px; top: 70px; width: 446px; height: 745px;
    background: linear-gradient(160deg, var(--pouch-light) 0%, var(--pouch-mid) 55%, var(--pouch-light) 100%);
    overflow: hidden;
  }
  .pouch-fade {
    position: absolute; left: 0; right: 0; bottom: 0; height: 80px;
    background: linear-gradient(180deg, rgba(227,23,27,0) 0%, rgba(227,23,27,0.10) 100%);
  }
  .tear-band {
    position: absolute; left: 0; right: 0; top: 56px; height: 34px;
    background: var(--brand-red); color: var(--white);
    font-size: 15px; letter-spacing: 1.6px; font-weight: 700;
    display: flex; align-items: center; justify-content: flex-end; padding-right: 26px;
  }
  .brand-name {
    position: absolute; left: 30px; top: 580px; width: 440px;
    transform: rotate(-90deg); transform-origin: 0 0;
    font-family: "Play", sans-serif; font-weight: 700; color: var(--brand-red);
    text-transform: uppercase; line-height: 1; font-size: 62px;
  }
  .brand-name span { display: block; }
  .brand-name .line-two { margin-top: 8px; }
  .divider {
    position: absolute; left: 188px; top: 115px; width: 2px; height: 465px;
    background: var(--brand-red);
  }
  .product-title {
    position: absolute; left: 203px; top: 138px;
    font-size: 30px; line-height: 1.22; font-weight: 700;
  }
  .tag {
    position: absolute; left: 203px; height: 24px;
    background: var(--brand-red); color: var(--white);
    font-weight: 700; display: flex; align-items: center;
    padding: 0 22px 0 6px; white-space: nowrap;
    clip-path: polygon(0 0, calc(100% - 14px) 0, 100% 50%, calc(100% - 14px) 100%, 0 100%);
  }
  .tag-flavour { top: 230px; font-size: 15px; letter-spacing: 0.4px; }
  .servings { position: absolute; left: 203px; top: 272px; }
  .servings-count { font-size: 50px; font-weight: 700; line-height: 1; }
  .servings-label { font-size: 14px; font-weight: 700; margin-top: 2px; }
  .weight { position: absolute; left: 290px; top: 300px; font-size: 22px; font-weight: 700; }
  .benefits { list-style: none; }
  .benefits .tag { height: 17px; font-size: 11.5px; padding-right: 14px;
    clip-path: polygon(0 0, calc(100% - 9px) 0, 100% 50%, calc(100% - 9px) 100%, 0 100%); }
  .benefit-1 { top: 357px; }
  .benefit-2 { top: 380px; }
  .benefit-3 { top: 403px; }
  .benefit-4 { top: 426px; }
  .ingredient-art {
    position: absolute; left: 200px; top: 445px; width: 220px; height: 245px;
    background: radial-gradient(ellipse at 28% 78%, rgba(200,36,42,0.9) 0%, rgba(176,69,58,0.6) 28%, rgba(230,230,230,0) 52%),
                radial-gradient(ellipse at 68% 50%, rgba(168,120,56,0.8) 0%, rgba(168,120,56,0) 55%);
  }
  .badges { position: absolute; left: 26px; top: 612px; display: flex; gap: 9px; }
  .badge { width: 40px; text-align: center; font-size: 8px; font-weight: 700; color: var(--brand-red); }
  .badge-shape {
    display: block; width: 36px; height: 36px; margin: 0 auto 8px;
    border: 2.5px solid var(--brand-red); border-radius: 50%;
  }
</style>
</head>
<body>
  <main class="pouch">
    <div class="pouch-fade"></div>
    <div class="tear-band">TEAR HERE &amp; RESEAL</div>

    <h1 class="brand-name">
      <span class="line-one">Stellar</span>
      <span class="line-two">Fuelworks</span>
    </h1>

    <div class="divider"></div>

    <h2 class="product-title">Natural<br>Whey Protein</h2>
    <div class="tag tag-flavour">STRAWBERRY FLAVOUR</div>

    <div class="servings">
      <div class="servings-count">30</div>
      <div class="servings-label">SERVINGS</div>
    </div>
    <div class="weight">909g</div>

    <ul class="benefits">
      <li class="tag benefit-1">No artificial Flavours</li>
      <li class="tag benefit-2">Excellent Amino acid profile</li>
      <li class="tag benefit-3">80% high quality protein content</li>
      <li class="tag benefit-4">Soy free</li>
    </ul>

    <div class="ingredient-art" role="img" aria-label="Fresh strawberries with ears of wheat and grains"></div>

    <div class="badges">
      <div class="badge"><span class="badge-shape"></span>PURE</div>
      <div class="badge"><span class="badge-shape"></span>PERSONAL</div>
      <div class="badge"><span class="badge-shape"></span>PROVEN</div>
    </div>
  </main>
</body>
</html>
```